A slider bar and icons to be used on the map

#Background
We are currently creating a website for tourists to Japan . Named "Maple Trove," It's a website where users can search for shrines and temples across Japan on the map. We are seeking designs for three icons(shrine icon, temple icon, and representing both shrine and temple icon) and a slider bar to be used on this site's map.
#Requirements
Cool and understandable icons and a slider bar that match the web design.
#Web Design Concept
Attached is a reference document.
#Desired Items
We need four items written below.
-Shrine icon
-Temple icon
-Icon representing both shrines and temples (expressed as a single icon)
-Slider bar
#Regarding the Slider Bar
It has two functions:
-Filter popular shrines and temples.
-Filiter shrines and temples with cool kanji.
We would like it to be able to filter from both the right and the left.
We want to express that moving to the right represents popularity or cool kanji. We'd like to express this on the slider bar as a design.
* reference> https://snaps.vextoro.io/k4TnQw8zLp2HsVbX7
Updates
Need extra days to review
Target Market(s)
Inbound tourists to Japan
Look and feel

```html
<!DOCTYPE html>
<html lang="en">
<head>
<meta charset="utf-8">
<title>Map Filter Sliders</title>
<link rel="stylesheet" href="https://fonts.googleapis.com/css2?family=Barlow:wght@400;500&display=swap">
<style>
  :root {
    --bg: #ffffff;
    --track-grey: #d1d2d4;
    --track-peach: #fbe4cf;
    --track-edge: #b9babc;
    --label: #7f8184;
    --icon: #d6d7d9;
    --knob: #ffffff;
    --knob-edge: #a7a9ac;
    --green: #7a9f35;
    --olive: #b5b324;
    --gold: #fdc50f;
    --amber: #f8ac24;
    --orange: #f39021;
    --coral: #ef6d3c;
    --vermilion: #ea5a35;
    --lemon: #fff200;
    --pink: #ec2279;
    --magenta: #e6008b;
  }
  html, body {
    margin: 0;
    width: 1200px;
    height: 1200px;
    overflow: hidden;
    background: var(--bg);
  }
  .canvas {
    position: relative;
    width: 1200px;
    height: 1200px;
    font-family: "Barlow", "DIN Alternate", sans-serif;
  }
  .track, .range, .knob, .icon-slot, .label { position: absolute; }
  .track {
    height: 24px;
    border-radius: 12px;
    background: var(--track-grey);
    box-shadow: inset 0 0 0 1px var(--track-edge);
  }
  .track--peach { background: var(--track-peach); box-shadow: none; }
  .range { height: 25px; }
  .knob {
    width: 42px;
    height: 42px;
    margin: -21px 0 0 -21px;
    border-radius: 50%;
    background: var(--knob);
    box-shadow: 0 0 0 1px var(--knob-edge);
  }
  .icon-slot {
    background: var(--icon);
    border-radius: 4px;
  }
  .icon-slot--temple { width: 50px; height: 50px; }
  .icon-slot--shrine { width: 45px; height: 42px; }
  .label {
    font-size: 20px;
    font-weight: 500;
    color: var(--label);
    letter-spacing: 0.3px;
    line-height: 1;
    white-space: nowrap;
  }

  .range--one { background: linear-gradient(90deg, var(--green) 0%, var(--olive) 8%, var(--gold) 22%, var(--amber) 50%, var(--coral) 92%, var(--vermilion) 100%); }
  .range--two { background: linear-gradient(90deg, var(--green) 0%, var(--olive) 10%, var(--gold) 24%, var(--amber) 52%, var(--coral) 88%, var(--vermilion) 100%); }
  .range--three { background: linear-gradient(90deg, var(--amber) 0%, var(--gold) 35%, var(--lemon) 62%, var(--gold) 90%, var(--amber) 100%); }
  .range--four { background: linear-gradient(90deg, var(--pink) 0%, var(--magenta) 32%, var(--pink) 45%, var(--coral) 60%, var(--orange) 72%, var(--orange) 100%); }
</style>
</head>
<body>
<main class="canvas">
  <section class="slider slider--one">
    <div class="icon-slot icon-slot--temple" style="left:267px;top:122px" role="img" aria-label="Temple map icon"></div>
    <div class="icon-slot icon-slot--shrine" style="left:900px;top:136px" role="img" aria-label="Shrine map icon"></div>
    <div class="track" style="left:156px;top:200px;width:952px"></div>
    <div class="range range--one" style="left:292px;top:199px;width:630px"></div>
    <div class="knob" style="left:292px;top:209px"></div>
    <div class="knob" style="left:922px;top:215px"></div>
    <span class="label" style="left:162px;top:238px">Popularity</span>
    <span class="label" style="right:86px;top:238px">Stylish Kanji</span>
  </section>

  <section class="slider slider--two">
    <div class="icon-slot icon-slot--temple" style="left:212px;top:397px" role="img" aria-label="Temple map icon"></div>
    <div class="icon-slot icon-slot--shrine" style="left:995px;top:407px" role="img" aria-label="Shrine map icon"></div>
    <div class="track track--peach" style="left:156px;top:471px;width:952px"></div>
    <div class="range range--two" style="left:237px;top:469px;width:780px"></div>
    <div class="knob" style="left:237px;top:479px"></div>
    <div class="knob" style="left:1017px;top:483px"></div>
    <span class="label" style="left:162px;top:509px">Popularity</span>
    <span class="label" style="right:86px;top:509px">Stylish Kanji</span>
  </section>

  <section class="slider slider--three">
    <div class="icon-slot icon-slot--temple" style="left:431px;top:655px" role="img" aria-label="Temple map icon"></div>
    <div class="icon-slot icon-slot--shrine" style="left:781px;top:672px" role="img" aria-label="Shrine map icon"></div>
    <div class="track" style="left:156px;top:735px;width:952px"></div>
    <div class="range range--three" style="left:456px;top:734px;width:347px"></div>
    <div class="knob" style="left:456px;top:744px"></div>
    <div class="knob" style="left:803px;top:744px"></div>
    <span class="label" style="left:162px;top:774px">Popularity</span>
    <span class="label" style="right:86px;top:774px">Stylish Kanji</span>
  </section>

  <section class="slider slider--four">
    <div class="icon-slot icon-slot--temple" style="left:160px;top:925px" role="img" aria-label="Temple map icon"></div>
    <div class="icon-slot icon-slot--shrine" style="left:883px;top:936px" role="img" aria-label="Shrine map icon"></div>
    <div class="track" style="left:139px;top:999px;width:952px"></div>
    <div class="range range--four" style="left:185px;top:998px;width:720px"></div>
    <div class="knob" style="left:185px;top:1014px"></div>
    <div class="knob" style="left:905px;top:1014px"></div>
    <span class="label" style="left:145px;top:1038px">Popularity</span>
    <span class="label" style="right:103px;top:1038px">Stylish Kanji</span>
  </section>
</main>
</body>
</html>
```